Business Card Design needed for logo design project

Our business needs a business card design. I'm not sure what format files are generally delivered back, but clearly I will need the ability to edit to add colleagues contact details.

Our logo is attached.

Brivanor is a 3D design services company, providing app, serious/educational game, VR and AR websites/applications to corporate clients.

Target Market(s)

Corporate blue-chip clients needing 3D design services

Industry/Entity Type

Business

Font styles to use
Sans Serif

Requirements
Must have
• Templated such that I can add details (name, phone number etc). Needs to include logo from previous project winner - attached.

```html
<!DOCTYPE html>
<html lang="en">
<head>
<meta charset="utf-8">
<title>Brivanor — Business Card Set</title>
<link rel="stylesheet" href="https://fonts.googleapis.com/css2?family=PT+Sans:ital,wght@0,400;0,700;1,400&display=swap">
<style>
  :root {
    --page: #ffffff;
    --card-white: #ffffff;
    --card-edge: #9a9a9a;
    --ink: #333333;
    --ink-soft: #444444;
    --brand-red: #e3232b;
    --red-glow: #ee1c25;
    --red-deep: #bf1e2e;
    --on-red: #ffffff;
  }
  * { margin: 0; padding: 0; box-sizing: border-box; }
  html, body { width: 1200px; height: 849px; overflow: hidden; background: var(--page); }
  body { position: relative; font-family: "PT Sans", Arial, sans-serif; color: var(--ink); }

  .card {
    position: absolute;
    width: 359px;
    height: 205px;
    border: 1px solid var(--card-edge);
    box-shadow: 0 6px 10px rgba(0,0,0,0.22);
    overflow: hidden;
  }
  .card--front { background: var(--card-white); }
  .card--back {
    background: radial-gradient(ellipse 60% 75% at 40% 45%, var(--red-glow) 0%, #d81f2a 55%, var(--red-deep) 100%);
    border-color: #a8303a;
  }
  .card--a { left: 190px; }
  .card--b { left: 651px; }
  .row-1 { top: 181px; }
  .row-2 { top: 464px; }

  .wordmark { position: absolute; display: flex; align-items: center; }
  .wordmark__dot { border-radius: 50%; flex: none; }
  .wordmark__name { font-weight: 400; letter-spacing: 0.5px; line-height: 1; }
  .wordmark--dark .wordmark__dot { background: var(--brand-red); }
  .wordmark--dark .wordmark__name { color: var(--ink); }
  .wordmark--light .wordmark__dot { background: var(--on-red); }
  .wordmark--light .wordmark__name { color: var(--on-red); }

  .person { position: absolute; }
  .person__name { font-weight: 700; line-height: 1; color: var(--ink); }
  .person__title { font-style: italic; letter-spacing: 2px; color: var(--ink-soft); line-height: 1; }

  .contacts { position: absolute; list-style: none; }
  .contacts li { display: flex; align-items: center; height: 20px; font-style: italic; font-size: 10px; color: var(--ink); }
  .contacts svg { width: 14px; height: 14px; margin-right: 5px; fill: var(--brand-red); flex: none; }

  .tagline-rule { position: absolute; left: 179px; top: 52px; width: 2px; height: 100px; background: var(--on-red); }
  .tagline { position: absolute; left: 192px; top: 64px; color: var(--on-red); font-size: 16px; line-height: 20.5px; }
</style>
</head>
<body>

<svg width="0" height="0" style="position:absolute" aria-hidden="true">
  <defs>
    <symbol id="icon-phone" viewBox="0 0 24 24"><path d="M6.6 10.8a15.2 15.2 0 0 0 6.6 6.6l2.2-2.2a1 1 0 0 1 1-.25 11.4 11.4 0 0 0 3.6.57 1 1 0 0 1 1 1V20a1 1 0 0 1-1 1A17 17 0 0 1 3 4a1 1 0 0 1 1-1h3.5a1 1 0 0 1 1 1c0 1.25.2 2.45.57 3.57a1 1 0 0 1-.25 1z"/></symbol>
    <symbol id="icon-mail" viewBox="0 0 24 24"><path d="M2 5h20v14H2z M2 5l10 8 10-8" stroke="#fff" stroke-width="1.5"/></symbol>
    <symbol id="icon-pin" viewBox="0 0 24 24"><path d="M12 1a8 8 0 0 0-8 8c0 6 8 14 8 14s8-8 8-14a8 8 0 0 0-8-8zm0 11a3 3 0 1 1 0-6 3 3 0 0 1 0 6z"/></symbol>
  </defs>
</svg>

<!-- Front, layout one -->
<section class="card card--front card--a row-1">
  <div class="wordmark wordmark--dark" style="left:22px; top:86px;">
    <span class="wordmark__dot" style="width:30px;height:30px;margin-right:7px;"></span>
    <span class="wordmark__name" style="font-size:24px;">BRIVANOR</span>
  </div>
  <div class="person" style="left:213px; top:41px;">
    <p class="person__name" style="font-size:16px;">Elias Marlow</p>
    <p class="person__title" style="font-size:11px;margin-top:7px;">Founder, CEO</p>
  </div>
  <ul class="contacts" style="left:213px; top:118px;">
    <li><svg><use href="#icon-phone"/></svg>0090 533 210 4417</li>
    <li><svg><use href="#icon-mail"/></svg>info@brivanor.com</li>
    <li><svg><use href="#icon-pin"/></svg>48C, Fenwick Lane</li>
  </ul>
</section>

<!-- Back, layout one -->
<section class="card card--back card--b row-1">
  <div class="wordmark wordmark--light" style="left:98px; top:86px;">
    <span class="wordmark__dot" style="width:33px;height:33px;margin-right:7px;"></span>
    <span class="wordmark__name" style="font-size:25px;">BRIVANOR</span>
  </div>
</section>

<!-- Front, layout two -->
<section class="card card--front card--a row-2">
  <div class="wordmark wordmark--dark" style="left:26px; top:26px;">
    <span class="wordmark__dot" style="width:39px;height:39px;margin-right:8px;"></span>
    <span class="wordmark__name" style="font-size:29px;">BRIVANOR</span>
  </div>
  <div class="person" style="left:26px; top:129px;">
    <p class="person__name" style="font-size:15px;">Elias Marlow</p>
    <p class="person__title" style="font-size:10px;margin-top:6px;">Founder, CEO</p>
  </div>
  <ul class="contacts" style="left:228px; top:127px;">
    <li><svg><use href="#icon-phone"/></svg>0090 533 210 4417</li>
    <li><svg><use href="#icon-mail"/></svg>info@brivanor.com</li>
    <li><svg><use href="#icon-pin"/></svg>48C, Fenwick Lane</li>
  </ul>
</section>

<!-- Back, layout two -->
<section class="card card--back card--b row-2">
  <div class="wordmark wordmark--light" style="left:32px; top:89px;">
    <span class="wordmark__dot" style="width:27px;height:27px;margin-right:6px;"></span>
    <span class="wordmark__name" style="font-size:21px;">BRIVANOR</span>
  </div>
  <span class="tagline-rule"></span>
  <p class="tagline">3D design<br>services<br>company</p>
</section>

</body>
</html>
```